Design a App to help people have successful dates!

We require an awesome designer to help us with an App design for a new dating app we are introducing! Our App is intended to help Users build confidence is knowing what questions or ask and answer when going on dates! As you can see from our Project Brief, the intent of the app is to display two types of content to the user 1) Dating Questions, and 2) Dating Tips. We have developed wireframes to help convey what each screen should convey. The intent is to 'inform' and 'educate' the User on what questions to ask, or what questions could be asked of them. Also, we would like to include Banner Ads on the 'Question' and 'Tip' screens, which you can see in the brief.

Target Market(s)

Men and women - aged 18 - 45 who need help identifying dating questions

Industry/Entity Type

Dating App

Font styles to use
Sans Serif

Requirements
Must have
• Please review the PDF brief that we have uploaded. Please make the swipe left and right feature modern (I only included the buttons as a guide only). The ‘Courtship Riddle Ace’ App is intended to be a light-hearted, simple, elegant, fun App, to help Users ask and engage in dating questions. Think of this app as an 'LoveBridgeo' (high quality, educated Users) to help users with identifying questions to ask on dates.
Nice to have
• Please review the PDF brief that we have uploaded.
Should not have
• The App is intended to only include genuine, legitimate, clean and appropriate content. This is not a 'Flimbo' stiyle look-up app.

```html
<!DOCTYPE html>
<html lang="en">
<head>
<meta charset="utf-8">
<title>Courtship Riddle Ace – App Screens</title>
<link rel="stylesheet" href="https://fonts.googleapis.com/css2?family=IBM+Plex+Sans:wght@400;600;700&display=swap">
<style>
  :root {
    --canvas: #e4eaf4;
    --brand-blue: #05a0e2;
    --navy: #363f51;
    --navy-soft: #4a5366;
    --paper: #f5f6fa;
    --ink: #2e3440;
    --white: #ffffff;
    --olive: #7fa20f;
    --ad-blue: #1e6fc4;
    --photo-warm-a: #3a2a2a;
    --photo-warm-b: #8a5a3e;
  }
  * { box-sizing: border-box; margin: 0; padding: 0; }
  html, body { width: 1200px; height: 556px; overflow: hidden; }
  body {
    background: var(--canvas);
    font-family: "IBM Plex Sans", Arial, sans-serif;
    position: relative;
    color: var(--ink);
  }
  .screen {
    position: absolute;
    overflow: hidden;
    box-shadow: 0 2px 8px rgba(40, 50, 80, .12);
  }
  .screen--light { background: var(--paper); }
  .screen--dark { background: var(--navy); }

  .app-bar {
    position: absolute; left: 0; top: 0; width: 100%; height: 34px;
    background: var(--brand-blue); color: var(--white);
    display: flex; align-items: center; justify-content: center;
    font-weight: 700; font-size: 12px; letter-spacing: .2px;
  }
  .app-bar__back {
    position: absolute; left: 8px; top: 0; height: 34px;
    display: flex; align-items: center; gap: 4px;
    font-weight: 600; font-size: 11px;
  }
  .app-bar__place { text-align: center; line-height: 1.15; }
  .app-bar__city { font-weight: 700; font-size: 9px; display: block; }
  .app-bar__time { font-weight: 400; font-size: 8px; display: block; }

  .hero-photo {
    position: absolute; left: 0; width: 100%;
    background: radial-gradient(circle at 70% 30%, #b27a52 0%, var(--photo-warm-b) 30%, var(--photo-warm-a) 80%);
  }
  .welcome-title {
    position: absolute; left: 0; width: 100%; text-align: center;
    font-weight: 700; color: var(--ink);
  }
  .welcome-sub {
    position: absolute; left: 0; width: 100%; text-align: center;
    font-weight: 400; color: var(--ink);
  }
  .btn {
    position: absolute; display: flex; align-items: center; justify-content: center; gap: 6px;
    color: var(--white); font-weight: 700; letter-spacing: .3px;
  }
  .btn--blue { background: var(--brand-blue); }
  .btn--olive { background: var(--olive); }

  .profile { position: absolute; width: 75px; text-align: center; }
  .profile__photo { width: 75px; height: 72px; }
  .profile__photo--light { background: linear-gradient(160deg, #eef0f2, #c9cfd6); }
  .profile__photo--grey { background: linear-gradient(160deg, #7c8794, #4f5966); }
  .profile__name {
    margin-top: 9px; color: var(--white); font-weight: 700; font-size: 9.5px; letter-spacing: .3px;
  }

  .card-shape { position: absolute; }
  .card-text {
    position: absolute; text-align: center; font-weight: 700; color: var(--ink);
    font-size: 13px; line-height: 18px; letter-spacing: .3px;
  }
  .swipe { position: absolute; width: 10px; height: 14px; }

  .tip-box {
    position: absolute; background: var(--navy-soft); border-radius: 3px;
    color: var(--white); font-size: 10.5px; line-height: 13.2px; text-align: center;
    padding: 17px 4px 0; white-space: nowrap;
  }

  .ad-banner {
    position: absolute; width: 201px; height: 33px; border-radius: 2px;
    background: linear-gradient(180deg, #3a8ae0, var(--ad-blue));
    border: 1px solid #b7cce6;
    display: flex; align-items: center; padding: 0 4px; gap: 4px; color: var(--white);
  }
  .ad-banner__brand {
    width: 24px; height: 24px; background: var(--white); border-radius: 3px;
    color: var(--ad-blue); font-size: 6px; font-weight: 600;
    display: flex; align-items: center; justify-content: center;
  }
  .ad-banner__copy { font-size: 7px; font-weight: 700; line-height: 9px; flex: 1; }
  .ad-banner__by { font-size: 5px; font-weight: 400; margin-right: 3px; }
  .ad-banner__get { width: 18px; height: 18px; }
</style>
</head>
<body>

<!-- Compact welcome screen -->
<section class="screen screen--light" style="left:40px; top:49px; width:143px; height:305px; border-radius:10px;">
  <div class="app-bar" style="height:21px; font-size:7px;">COURTSHIP RIDDLE ACE</div>
  <div class="hero-photo" role="img" aria-label="Smiling couple sharing a cosy candlelit date" style="top:21px; height:172px;"></div>
  <div class="welcome-title" style="top:216px; font-size:8.5px;">COURTSHIP RIDDLE ACE</div>
  <div class="welcome-sub" style="top:232px; font-size:7.5px;">No awkward silences</div>
  <div class="btn btn--blue" style="left:6px; top:292px; width:129px; height:13px; font-size:6px;">GET STARTED</div>
</section>

<!-- Welcome screen -->
<section class="screen screen--light" style="left:209px; top:32px; width:225px; height:487px;">
  <header class="app-bar">COURTSHIP RIDDLE ACE</header>
  <div class="hero-photo" role="img" aria-label="Smiling couple sharing a cosy candlelit date" style="top:34px; height:257px;"></div>
  <h1 class="welcome-title" style="top:326px; font-size:14px;">COURTSHIP RIDDLE ACE</h1>
  <p class="welcome-sub" style="top:348px; font-size:12.5px;">No awkward silences</p>
  <a class="btn btn--blue" style="left:17px; top:438px; width:192px; height:34px; font-size:13px;">GET STARTED
    <svg width="11" height="10" viewBox="0 0 11 10" fill="none" stroke="#fff" stroke-width="1.6"><path d="M1 1l4 4-4 4M6 1l4 4-4 4"/></svg>
  </a>
</section>

<!-- Menu screen -->
<section class="screen screen--dark" style="left:455px; top:32px; width:225px; height:487px;">
  <header class="app-bar">
    <span class="app-bar__back"><svg width="7" height="11" viewBox="0 0 7 11" fill="none" stroke="#fff" stroke-width="1.6"><path d="M6 1L1.5 5.5 6 10"/></svg>Back</span>
    <span class="app-bar__place"><span class="app-bar__city">SAN FRANCISCO</span><span class="app-bar__time">26 July 6:26 AM</span></span>
  </header>
  <div class="profile" style="left:29px; top:105px;"><div class="profile__photo profile__photo--light" role="img" aria-label="Profile photo of a man"></div><div class="profile__name">LOREM</div></div>
  <div class="profile" style="left:113px; top:105px;"><div class="profile__photo profile__photo--grey" role="img" aria-label="Profile photo of a woman"></div><div class="profile__name">LOREM</div></div>
  <div class="profile" style="left:29px; top:225px;"><div class="profile__photo profile__photo--light" role="img" aria-label="Profile photo of a man with glasses"></div><div class="profile__name">LOREM</div></div>
  <div class="profile" style="left:113px; top:225px;"><div class="profile__photo profile__photo--light" role="img" aria-label="Profile photo of a blonde woman"></div><div class="profile__name">LOREM</div></div>
  <a class="btn btn--blue" style="left:16px; top:387px; width:193px; height:34px; font-size:12.5px;">DATING QUESTIONS
    <svg width="11" height="10" viewBox="0 0 11 10" fill="none" stroke="#fff" stroke-width="1.6"><path d="M1 1l4 4-4 4M6 1l4 4-4 4"/></svg>
  </a>
  <a class="btn btn--olive" style="left:16px; top:431px; width:193px; height:34px; font-size:12.5px;">DATING TIPS</a>
</section>

<!-- Question screen -->
<section class="screen screen--dark" style="left:706px; top:32px; width:225px; height:487px;">
  <header class="app-bar">
    <span class="app-bar__back"><svg width="7" height="11" viewBox="0 0 7 11" fill="none" stroke="#fff" stroke-width="1.6"><path d="M6 1L1.5 5.5 6 10"/></svg>Back</span>
    <span class="app-bar__place"><span class="app-bar__city">SAN FRANCISCO</span><span class="app-bar__time">26 July 6:26 AM</span></span>
  </header>
  <svg class="swipe" style="left:11px; top:210px;" viewBox="0 0 10 14" fill="none" stroke="#fff" stroke-width="1.6"><path d="M8 1L2 7l6 6"/></svg>
  <svg class="card-shape" style="left:35px; top:155px;" width="155" height="153" viewBox="0 0 155 153"><path d="M14 0H141Q155 0 155 14V140Q155 153 142 150L12 125Q0 122 0 110V14Q0 0 14 0Z" fill="#f5f6fa"/></svg>
  <div class="card-text" style="left:35px; top:201px; width:155px;">WHAT MAKES<br>YOU LAUGH?</div>
  <svg class="swipe" style="left:203px; top:210px;" viewBox="0 0 10 14" fill="none" stroke="#fff" stroke-width="1.6"><path d="M2 1l6 6-6 6"/></svg>
  <div class="ad-banner" style="left:11px; top:442px;">
    <div class="ad-banner__brand">Quirra</div>
    <div class="ad-banner__copy">1000's of Free Books!<br>Download App!</div>
    <span class="ad-banner__by">Ads by AdLoop</span>
    <svg class="ad-banner__get" viewBox="0 0 18 18"><circle cx="9" cy="9" r="8" fill="#1c2838" stroke="#fff" stroke-width="1"/><path d="M9 4v8M5.5 9L9 12.5 12.5 9" stroke="#fff" stroke-width="1.5" fill="none"/></svg>
  </div>
</section>

<!-- Tip screen -->
<section class="screen screen--dark" style="left:947px; top:32px; width:225px; height:487px;">
  <header class="app-bar">
    <span class="app-bar__back"><svg width="7" height="11" viewBox="0 0 7 11" fill="none" stroke="#fff" stroke-width="1.6"><path d="M6 1L1.5 5.5 6 10"/></svg>Back</span>
    <span class="app-bar__place"><span class="app-bar__city">SAN FRANCISCO</span><span class="app-bar__time">26 July 6:26 AM</span></span>
  </header>
  <svg class="swipe" style="left:12px; top:130px;" viewBox="0 0 10 14" fill="none" stroke="#fff" stroke-width="1.6"><path d="M8 1L2 7l6 6"/></svg>
  <svg class="card-shape" style="left:36px; top:105px;" width="154" height="79" viewBox="0 0 154 79"><path d="M13 0H141Q154 0 154 13V66Q154 79 141 78L12 66Q0 65 0 53V13Q0 0 13 0Z" fill="#f5f6fa"/></svg>
  <div class="card-text" style="left:36px; top:120px; width:154px;">ARRIVE TO THE<br>DATE ON TIME.</div>
  <svg class="swipe" style="left:204px; top:130px;" viewBox="0 0 10 14" fill="none" stroke="#fff" stroke-width="1.6"><path d="M2 1l6 6-6 6"/></svg>
  <div class="tip-box" style="left:20px; top:224px; width:186px; height:122px;">
    Don’t be one of those<br>‘fashionably late’ people.<br>Your date may feel nervous or<br>anxious whether you are even<br>coming. Make sure you arrive<br>to meet your date on time.
  </div>
  <div class="ad-banner" style="left:12px; top:442px;">
    <div class="ad-banner__brand">Quirra</div>
    <div class="ad-banner__copy">1000's of Free Books!<br>Download App!</div>
    <span class="ad-banner__by">Ads by AdLoop</span>
    <svg class="ad-banner__get" viewBox="0 0 18 18"><circle cx="9" cy="9" r="8" fill="#1c2838" stroke="#fff" stroke-width="1"/><path d="M9 4v8M5.5 9L9 12.5 12.5 9" stroke="#fff" stroke-width="1.5" fill="none"/></svg>
  </div>
</section>

</body>
</html>
```